CV Template

We need a graphic design to our new CV templates for our consultants. We are a small young Danish upcoming IT-business company making software solutions for our customers etc. You can visit our new website here: dev.lunavaerket.com, then you can see our web design, colors etc. I have attached a file for your inspiration :-) In the presentation I would like to have a picture of the employee, some text who descripe the profile/consultant and then I imagine that there is a table where we can write the employee's skills etc.

I would like the design to be "fresh & catchy" :-)

Looking forward to hear from you.

Best regards,
Sanne

```html
<!DOCTYPE html>
<html lang="da">
<head>
<meta charset="utf-8">
<title>CV – Lunaværket ApS</title>
<link rel="stylesheet" href="https://fonts.googleapis.com/css2?family=Gelasio:wght@700&family=Arimo:wght@400&display=swap">
<style>
  :root {
    --accent: #6fc6dc;
    --band: #6ccde0;
    --ink: #1a1a1a;
    --rule: #a9a9a9;
    --paper: #ffffff;
  }
  * { margin: 0; padding: 0; box-sizing: border-box; }
  html, body { width: 849px; height: 1200px; overflow: hidden; background: var(--paper); }
  .page { position: relative; width: 849px; height: 1200px; font-family: "Arimo", Arial, sans-serif; color: var(--ink); }

  .section { position: absolute; }
  .section-head { display: flex; align-items: center; gap: 29px; height: 30px; }
  .section-head svg { width: 26px; height: 26px; flex: none; }
  .section-title { font-family: "Gelasio", Georgia, serif; font-weight: 700; font-size: 19.5px; color: var(--accent); }
  .section p { font-size: 12.8px; line-height: 18.6px; }
  .section p + p { margin-top: 18.6px; }

  .rule-h { position: absolute; height: 4px;
    background: repeating-linear-gradient(90deg, var(--rule) 0 4px, transparent 4px 7.5px); }
  .rule-v { position: absolute; width: 4px;
    background: repeating-linear-gradient(180deg, var(--rule) 0 4px, transparent 4px 7.5px); }

  .footer { position: absolute; left: 40px; top: 1105px; width: 766px; height: 46px; background: var(--band);
    display: flex; align-items: center; justify-content: center; gap: 24px;
    color: #fff; font-size: 11px; letter-spacing: 0.3px; }
</style>
</head>
<body>
<div class="page">

  <section class="section education" style="left:40px; top:42px; width:368px;">
    <div class="section-head">
      <svg viewBox="0 0 26 26"><circle cx="13" cy="13" r="13" fill="#1a1a1a"/><path d="M13 7.5v11M7.5 13h11" stroke="#fff" stroke-width="2.6"/></svg>
      <h2 class="section-title">Uddannelse</h2>
    </div>
    <p style="margin-top:26px; letter-spacing:-0.3px;">Uddannet som datalog/cand. scient ved Nordhavn Universitet februar 1989, hovedfag datalogi, bifag matematik.</p>
  </section>
  <div class="rule-h" style="left:40px; top:159px; width:368px;"></div>

  <section class="section certificates" style="left:40px; top:195px; width:368px;">
    <div class="section-head">
      <svg viewBox="0 0 26 26"><circle cx="13" cy="13" r="13" fill="#1a1a1a"/><path d="M13 7.5v11M7.5 13h11" stroke="#fff" stroke-width="2.6"/></svg>
      <h2 class="section-title">Certificeringer</h2>
    </div>
    <p style="margin-top:14px;">Ingen certificeringer</p>
  </section>
  <div class="rule-h" style="left:40px; top:288px; width:368px;"></div>

  <section class="section experience" style="left:40px; top:320px; width:370px;">
    <div class="section-head">
      <svg viewBox="0 0 26 26"><circle cx="13" cy="13" r="13" fill="#1a1a1a"/><path d="M13 7.5v11M7.5 13h11" stroke="#fff" stroke-width="2.6"/></svg>
      <h2 class="section-title">Erhvervs erfaringer</h2>
    </div>
    <div style="margin-top:26px;">
      <p>Været selvstændig i 25 år med egen virksomhed hvor forretningsområdet primært bestod i udvikling af kundespecifikke applikationer til PC, Solux og WEB primært baseret på Vebas Studio, Skript, Javik, Phora, DataQL, MinQL, Orakul, Arkivbase, Paradis.</p>
      <p>Eksempler på udviklingsprojekter:</p>
      <p>A. WEB-baseret pakkelistesystem til Kalkværk Industri med mulighed for leverandørregistreringer og opfølgning (shipping/expediting) hos Kalkværk Industri. Tilsvarende system udviklet til Brandt Katalyse.</p>
      <p>B. Kørselsregistreringssystem udviklet i Vebas Studio som Vindo-applikation til Statsforsvaret.</p>
      <p>C. Beregnings- og administrationsprogrammer til De Nordiske Hobbyforeninger (i dag også anvendt i Sverige og Norge), dels som Vindo-applikationer, dels WEB på Solux-server.</p>
    </div>
  </section>

  <div class="rule-v" style="left:432px; top:46px; height:752px;"></div>

  <section class="section profile" style="left:452px; top:42px; width:354px;">
    <div class="section-head">
      <svg viewBox="0 0 26 26"><circle cx="13" cy="13" r="13" fill="#1a1a1a"/><path d="M13 7.5v11M7.5 13h11" stroke="#fff" stroke-width="2.6"/></svg>
      <h2 class="section-title">Profilbeskrivelse</h2>
    </div>
    <p style="margin-top:14px; line-height:19.2px;">Erfaren software udvikler med 25 års erfaring, som selvstændig hvor han bl.a. har arbejdet med udvikling af kundespecifikke applikationer til PC til WEB i samarbejde med kunder/brugere. Derudover stor erfaring med analyse, design, programmering, test, uddannelse/undervisning, kundesupport og projektledelse. Ud over at være en dygtig software udvikler er han også en stabil og rutineret konsulent, som er vant til, at yde konsulentbistand, support og udvikling af softwareløsninger til PC, Solux og WEB.</p>
  </section>
  <div class="rule-h" style="left:452px; top:288px; width:354px;"></div>

  <section class="section languages" style="left:452px; top:320px; width:354px;">
    <div class="section-head">
      <svg viewBox="0 0 26 26"><circle cx="13" cy="13" r="13" fill="#1a1a1a"/><path d="M13 7.5v11M7.5 13h11" stroke="#fff" stroke-width="2.6"/></svg>
      <h2 class="section-title">Sprog</h2>
    </div>
    <p style="margin-top:22px;">Dansk: Modersmål i både tale- og skrift<br>Engelsk: Behersker det i både tale- og skrift</p>
  </section>

  <div class="rule-h" style="left:40px; top:818px; width:766px;"></div>

  <footer class="footer">
    <span>Lunaværket ApS</span>
    <span>Solsortvej 12</span>
    <span>2200 København N.</span>
    <span style="margin-left:10px;">Tel: +45 20 14 37 90</span>
    <span>www.lunavaerket.dk</span>
  </footer>

</div>
</body>
</html>
```